Lantern Hours Cigar Portfolio

Subject Line:
🎉 Elevate Your Lounge Experience with Lantern Hours Cigars & Custom Accessories

Email Body:
Dear [Recipient Name],
KMWR Traders are excited to introduce our Lantern Hours with Customizable Cigar Swag Packages – designed to elevate your brand, engage your customers, and simplify inventory management.
Harbor and Flint’s Lantern Hours Portfolio — a curated line of cigars and accessories designed to celebrate life’s moments, big and small.
Whether you're stocking up for your lounge, prepping for an event, or looking to offer your customers something truly collectible, Lantern Hours delivers premium quality, customizable packaging, and a versatile smoking experience.

Why Lantern Hours?
✔️ Four Signature Blends
Each blend is crafted for different times of day and occasions:
• Connecticut – Smooth & creamy for the morning
• Habano – Spicy & balanced for any time
• Sumatra – Earthy & sweet for the afternoon
• Maduro – Bold & rich for the evening
👉 View Taste Profiles (Link to landing page with full flavor descriptions)

🔥 Product Highlights
1. Collectible Tins
• Periodically evolving artwork
• Magnetic matchboxes inside (16–20 matches, QAV carry-on approved)
• Reload QR label behind cigars for easy reordering
• Creates a secondary collectible market
2. Magnetic Koozies
• Attach directly to your tins
3. Tote Drawstring Bags
• Durable, water-resistant
• Zippered compartment for convenience
4. Colored Bar Globes w/Matches
• Eye-catching display pieces
• Includes free matches with every reorder
5. Free Matches
• Included with every order
• Refill anytime, no extra charge
6. QR Code Convenience
• Your QR code, not ours
• Drop-shipped directly to your customers or to your shop for in-person pickup

🧠 Tiered Options & Pricing

Tier Contents Cost/Value MSRP Value
Lantern Hours 20ct Bundle $100 $200
Tier 1 2 of each bundle (10 loaded tins) $1010 / $1050 —
Tier 2 4 of each bundle (35 loaded tins), 15 koozies, 15 bags, 4 bar globes. Your logo 2.5”x2.5” included on back of tin. $2395 / $2672.50 —
Tier 3 6 of each bundle (70 loaded tins), 70 koozies, 70 bags, 4 bar globes, reload QR codes, branded landing page. Your logo 2.5”x2.5” included on back of tin. $3995/ $5000

🎨 Tier 3 Bonus Features
1. Branded Landing Page: Created just for your lounge.
2. Easter Egg Graphics: Hidden artwork rewards customers with free cigars when identified.
3. Custom Tin Orders: Eligible with orders of 35+ tins (submit your own artwork)
Starting at $375 with a retail value of $875.
📎 Pricing Sheet Attached

Let’s Celebrate Together
We’d love to help you bring Lantern Hours to your customers. Reply to this email or schedule a quick call to explore options and request samples.
Cheers,
[CSR Name]
KMWR Traders
[CSR Email] | [Phone Number]
[Company Website or Landing Page]

Toro: 6 x 54
Connecticut wrapper Ecuador
Habano binder Jalapa
Filler Esteli and Jalapa

Toro: 6 x 54
Habano wrapper Ecuador
Binder Indonesia
Filler Esteli, Pueblo Nuevo

Toro: 6 x 54
Sumatra wrapper Indonesia
Filler habano Ecuador
Filler Esteli , ometepe

Toro: 6 x 54
Maduro wrapper Brazil
Binder Sumatra
Filler Esteli , Condega, Jalapa

Packaging
Lantern Hours cigars are available in three convenient packaging options:
• By the Bundle: Ideal for regular smokers who appreciate the value and quality of our cigars.
• Customized 4-Cigar Lantern Hour Tin: Perfect for gifting or special occasions, these tins can be personalized to add a unique touch to your celebration.
• Custom Box: A perfect offering for an event “grab” with all whom you are celebrating with, making it easy to share the joy of Lantern Hours cigars.
Harbor and Flint’s Lantern Hours line is all about celebrating moments, big and small. With a cigar for every time of the day and any special occasion, Lantern Hours ensures that every smoke is a memorable experience. Whether you're on the golf course, the water, a hunt, or just lounging, Lantern Hours cigars are the perfect companions for life's cherished moments.

```html
<!DOCTYPE html>
<html lang="en">
<head>
<meta charset="utf-8">
<title>Lantern Hours Cigar Portfolio</title>
<link href="https://fonts.googleapis.com/css2?family=Cinzel:wght@600;700&family=Poppins:wght@400;500;600&family=Bebas+Neue&display=swap" rel="stylesheet">
<style>
:root{
  --navy:#1c2237;
  --tan:#b59672;
  --tan-light:#c9ab86;
  --white:#ffffff;
  --card:#f3f4f9;
  --ink:#1c2237;
  --stage:#cacaca;
}
*{margin:0;padding:0;box-sizing:border-box}
html,body{width:1200px;height:2245px;overflow:hidden;background:var(--stage)}
body{position:relative;font-family:"Poppins",sans-serif;color:var(--ink)}
.column{position:absolute;top:150px;width:373px;background:var(--white);overflow:hidden}
.column--left{left:194px;height:1944px}
.column--right{left:633px;height:1332px}
.column-bg{position:absolute;left:0;top:0}
.abs{position:absolute}
.serif{font-family:"Cinzel",serif;font-weight:700}
.section-title{position:absolute;left:0;width:373px;display:flex;align-items:center;justify-content:center;gap:8px;font-family:"Cinzel",serif;font-weight:700;font-size:17px;line-height:20px;letter-spacing:.3px}
.section-title::before,.section-title::after{content:"";width:30px;height:1.5px;background:var(--tan)}
.section-title.on-navy{color:var(--white)}
.section-title.on-white{color:var(--navy)}
.center-line{position:absolute;left:0;width:373px;text-align:center}
.body-text{font-size:7.6px;line-height:13.5px;color:var(--ink)}
.small{font-size:7px;line-height:10px}
.logo-ring{position:absolute;border:2px solid var(--tan);border-radius:50%;display:flex;align-items:center;justify-content:center;text-align:center;font-family:"Cinzel",serif;font-weight:700;color:var(--tan)}
.photo{position:absolute;border-radius:50%;border:3px solid var(--tan)}
.product-head{position:absolute;font-size:11px;font-weight:500;color:var(--navy);line-height:13px;letter-spacing:-.1px}
.tick-list{position:absolute;list-style:none}
.tick-list li{position:relative;padding-left:18px;font-size:7.4px;line-height:9.6px;color:var(--ink);margin-bottom:4.5px}
.tick-list li::before{content:"";position:absolute;left:0;top:0;width:9px;height:9px;border-radius:50%;background:var(--tan)}
.tick-list li::after{content:"";position:absolute;left:3px;top:2px;width:2px;height:4px;border:solid var(--white);border-width:0 1.2px 1.2px 0;transform:rotate(45deg)}
.blend-icon{position:absolute;width:22px;height:22px;border-radius:50%;background:var(--tan);border:1.5px solid var(--white)}
.blend-label{position:absolute;width:90px;font-size:6.2px;line-height:7px;color:var(--white)}
.blend-label b{display:block;font-weight:600;font-size:6.8px;margin-bottom:1px}
.pill{position:absolute;background:var(--tan);color:var(--white);font-size:8px;font-weight:600;border-radius:12px;display:flex;align-items:center;justify-content:center}
.tier-mark{position:absolute;width:14px;height:14px;border-radius:50%;border:1.2px solid var(--tan);left:179.5px}
.tier-text{font-size:7.4px;line-height:10.5px;color:var(--white)}
.num-badge{position:absolute;width:48px;height:48px;border-radius:50%;background:var(--navy);border:3px solid var(--white);box-shadow:0 0 0 2.5px var(--tan);color:var(--white);font-size:17px;font-weight:600;display:flex;align-items:center;justify-content:center}
.feature-title{position:absolute;font-size:9.2px;font-weight:500;color:var(--navy)}
.feature-desc{position:absolute;font-size:7px;line-height:10.5px;color:#444a5c}
.field{position:absolute;background:var(--white);border-radius:2px;font-size:6.2px;color:#9a9eaa;padding:8px 10px}
.form-label{position:absolute;left:32px;font-size:7.4px;color:var(--white)}
.toro-card{position:absolute;width:146px;height:113px;background:var(--card);border-radius:8px;text-align:center}
.toro-badge{position:absolute;width:62px;height:62px;border-radius:50%;background:var(--navy);border:3px solid var(--white);box-shadow:0 0 0 2.5px var(--tan);display:flex;flex-direction:column;align-items:center;justify-content:center;font-family:"Bebas Neue",sans-serif;line-height:15px}
.toro-badge .cut{color:var(--tan);font-size:16px}
.toro-badge .size{color:var(--white);font-size:17px}
.toro-title{position:absolute;left:0;width:146px;top:44px;font-size:10.2px;font-weight:600;line-height:12.5px;color:var(--navy)}
.toro-list{position:absolute;left:22px;top:77px;list-style:none;text-align:left}
.toro-list li{position:relative;padding-left:9px;font-size:7.4px;line-height:13.5px;color:var(--ink)}
.toro-list li::before{content:"";position:absolute;left:0;top:5px;width:4px;height:4px;border-radius:50%;background:var(--tan)}
.pack-list{position:absolute;left:37px;top:1138px;list-style:none;width:300px}
.pack-list li{position:relative;padding-left:11px;margin-bottom:5px}
.pack-list li::before{content:"";position:absolute;left:0;top:2px;width:9px;height:9px;border-radius:50%;background:var(--tan)}
.pack-list li::after{content:"";position:absolute;left:3px;top:4px;width:2px;height:4px;border:solid var(--navy);border-width:0 1.2px 1.2px 0;transform:rotate(45deg)}
.pack-list .pack-name{display:block;font-size:8.6px;font-weight:500;color:var(--tan);line-height:12px}
.pack-list .pack-desc{display:block;font-size:7.2px;line-height:9.5px;color:var(--white)}
</style>
</head>
<body>

<!-- LEFT PANEL -->
<section class="column column--left">
  <svg class="column-bg" width="373" height="1944" viewBox="0 0 373 1944" aria-hidden="true">
    <path d="M0 0H373V300C362 262 332 244 292 244H60C25 244 0 230 0 204Z" fill="var(--tan)"/>
    <path d="M0 0H373V294C362 256 332 238 292 238H60C25 238 0 224 0 198Z" fill="var(--navy)"/>
    <path d="M0 437C0 464 25 477 60 477H292C332 477 362 489 373 506V841C362 822 332 815 292 815H60C25 815 0 801 0 771Z" fill="var(--tan)"/>
    <path d="M0 443C0 470 25 483 60 483H292C332 483 362 495 373 512V835C362 816 332 809 292 809H60C25 809 0 795 0 765Z" fill="var(--navy)"/>
    <path d="M0 1544C0 1572 25 1587 60 1587H292C332 1587 362 1597 373 1613V1948H0Z" fill="var(--tan)"/>
    <path d="M0 1550C0 1578 25 1593 60 1593H292C332 1593 362 1603 373 1619V1942C362 1922 332 1915 292 1915H60C25 1915 0 1905 0 1881Z" fill="var(--navy)"/>
    <path d="M0 1881C0 1905 25 1915 60 1915H292C332 1915 362 1922 373 1942V1948C362 1928 332 1921 292 1921H60C25 1921 0 1911 0 1887Z" fill="var(--tan)"/>
  </svg>

  <header>
    <div class="logo-ring" style="left:149px;top:14px;width:74px;height:74px;font-size:8px;line-height:10px">Harbor<br>and Flint</div>
    <div class="section-title" style="top:108px;color:var(--tan);font-size:18px">Elevate</div>
    <div class="center-line serif" style="top:130px;font-size:18.5px;color:var(--white)">YOUR LOUNGE EXPERIENCE</div>
    <div class="center-line serif" style="top:151px;font-size:26px;line-height:30px;color:var(--tan)">WITH LANTERN HOURS</div>
    <div class="center-line serif" style="top:183px;font-size:17.5px;color:var(--white)">CIGARS &amp; CUSTOM ACCESSORIES</div>
  </header>

  <div class="abs body-text" style="left:18px;top:274px;width:320px;font-weight:500">Dear [Recipient Name],</div>
  <p class="abs body-text" style="left:18px;top:297px;width:320px;text-align:justify">KMWR Traders are excited to introduce our Lantern Hours with Customizable Cigar Swag Packages – designed to elevate your brand, engage your customers, and simplify inventory management.</p>
  <p class="abs body-text" style="left:18px;top:351px;width:320px">Harbor and Flint’s Lantern Hours Portfolio — a curated line of cigars and accessories designed to celebrate life’s moments, big and small.</p>
  <p class="abs body-text" style="left:18px;top:391px;width:320px">Whether you're stocking up for your lounge, prepping for an event, or looking to offer your customers something truly collectible, Lantern Hours delivers premium quality, customizable packaging, and a versatile smoking experience.</p>

  <section>
    <div class="section-title on-navy" style="top:533px">Why Lantern Hours?</div>
    <div class="center-line" style="top:574px;font-size:9.2px;font-weight:500;color:var(--tan)">FOUR SIGNATURE BLENDS</div>
    <div class="center-line" style="top:590px;font-size:7.4px;color:var(--white)">Each blend is crafted for different times of day and occasions:</div>

    <div class="abs" style="left:131px;top:613px;width:110px;height:110px;border-radius:50%;border:1.2px solid var(--white)"></div>
    <div class="logo-ring" style="left:137px;top:619px;width:98px;height:98px;font-size:10px;line-height:13px">Harbor<br>and Flint</div>

    <div class="blend-label" style="left:3px;top:626px;text-align:right"><b>Connecticut</b>Smooth &amp; creamy<br>for the morning</div>
    <div class="blend-icon" style="left:100px;top:630px"></div>
    <div class="blend-label" style="left:3px;top:675px;text-align:right"><b>Habano</b>Spicy &amp; balanced for<br>any time</div>
    <div class="blend-icon" style="left:100px;top:678px"></div>
    <div class="blend-icon" style="left:250px;top:630px"></div>
    <div class="blend-label" style="left:282px;top:626px"><b>Sumatra</b>Earthy &amp; sweet for<br>the afternoon</div>
    <div class="blend-icon" style="left:250px;top:678px"></div>
    <div class="blend-label" style="left:282px;top:675px"><b>Maduro</b>Bold &amp; rich for the<br>evening</div>

    <div class="pill" style="left:132px;top:741px;width:108px;height:21px">View Taste Profiles</div>
  </section>

  <section>
    <div class="section-title on-white" style="top:857px">Products</div>

    <div class="photo" role="img" aria-label="Stacked collectible cigar tins in red, blue and gold" style="left:202px;top:894px;width:210px;height:210px;background:linear-gradient(180deg,#c8202e 0%,#2a3f9a 22%,#d7b877 40%,#9b6a3c 70%,#c8202e 100%)"></div>
    <div class="product-head" style="left:17px;top:918px">1.&nbsp; COLLECTIBLE TINS</div>
    <ul class="tick-list" style="left:31px;top:943px;width:175px">
      <li>Periodically evolving artwork</li>
      <li>Magnetic matchboxes inside (16–20 matches, QAV carry-on approved)</li>
      <li>Reload QR label behind cigars for easy reordering</li>
      <li>Creates a secondary collectible market</li>
    </ul>
    <div class="product-head" style="left:17px;top:1036px">2.&nbsp; MAGNETIC KOOZIES</div>
    <ul class="tick-list" style="left:31px;top:1062px;width:175px">
      <li>Attach directly to your tins</li>
    </ul>

    <div class="photo" role="img" aria-label="Blue, red and yellow drawstring tote bags" style="left:-48px;top:1118px;width:212px;height:212px;background:linear-gradient(120deg,#2b4a9a 0%,#d9262e 40%,#f2d313 70%,#3a3a3a 100%)"></div>
    <div class="product-head" style="left:175px;top:1158px">3.&nbsp; TOTE DRAWSTRING BAGS</div>
    <ul class="tick-list" style="left:189px;top:1184px;width:160px">
      <li>Durable, water-resistant</li>
      <li>Zippered compartment for convenience</li>
    </ul>
    <div class="product-head" style="left:175px;top:1235px">4.&nbsp; COLORED BAR GLOBES<br>&nbsp;&nbsp;&nbsp;&nbsp;W/MATCHES</div>
    <ul class="tick-list" style="left:189px;top:1272px;width:160px">
      <li>Eye-catching display pieces</li>
      <li>Includes free matches with every reorder</li>
    </ul>

    <div class="photo" role="img" aria-label="Colored glass bar globes with matches beside open cigar tins" style="left:201px;top:1339px;width:212px;height:212px;background:linear-gradient(160deg,#8a7a68 0%,#5b4a3e 35%,#c9a58a 60%,#3c3a44 100%)"></div>
    <div class="product-head" style="left:19px;top:1383px">5.&nbsp; FREE MATCHES</div>
    <ul class="tick-list" style="left:33px;top:1409px;width:175px">
      <li>Included with every order</li>
      <li>Refill anytime, no extra charge</li>
    </ul>
    <div class="product-head" style="left:17px;top:1449px">6.&nbsp; QR CODE CONVENIENCE</div>
    <ul class="tick-list" style="left:33px;top:1475px;width:175px">
      <li>Your QR code, not ours</li>
      <li>Drop-shipped directly to your customers to your shop for in-person pickup</li>
    </ul>
  </section>

  <section>
    <div class="section-title on-navy" style="top:1635px;font-size:17.5px">Tiered Options &amp; Pricing</div>
    <div class="center-line" style="top:1676px;font-size:9.2px;font-weight:500;color:var(--tan)">TIER CONTENTS COST/VALUE MSRP VALUE</div>
    <div class="center-line" style="top:1691px;font-size:13.5px;font-weight:500;color:var(--white)">LANTERN HOURS 20CT BUNDLE $100 $200</div>

    <div class="tier-mark" style="top:1726px"></div>
    <div class="center-line tier-text" style="top:1747px">Tier 1 2 of each bundle (10 loaded tins) $1010 / $1050 —</div>
    <div class="tier-mark" style="top:1769px"></div>
    <div class="center-line tier-text" style="top:1790px">Tier 2 4 of each bundle (35 loaded tins), 15 koozies, 15 bags, 4 bar globes.<br>Your logo 2.5”x2.5” included on back of tin. $2395 / $2672.50 —</div>
    <div class="tier-mark" style="top:1821px"></div>
    <div class="center-line tier-text" style="top:1841px">Tier 3 6 of each bundle (70 loaded tins), 70 koozies, 70 bags,<br>4 bar globes, reload QR codes, branded landing page.<br>Your logo 2.5”x2.5” included on back of tin. $3995/ $5000</div>
  </section>
</section>

<!-- RIGHT PANEL -->
<section class="column column--right">
  <svg class="column-bg" width="373" height="1332" viewBox="0 0 373 1332" aria-hidden="true">
    <path d="M0 271C0 302 25 318 60 318H292C332 318 362 327 373 341V688C362 670 332 662 292 662H60C25 662 0 646 0 614Z" fill="var(--tan)"/>
    <path d="M0 277C0 308 25 324 60 324H292C332 324 362 333 373 347V682C362 664 332 656 292 656H60C25 656 0 640 0 608Z" fill="var(--navy)"/>
    <path d="M0 986C0 1018 25 1034 60 1034H292C332 1034 362 1044 373 1060V1332H0Z" fill="var(--tan)"/>
    <path d="M0 992C0 1024 25 1040 60 1040H292C332 1040 362 1050 373 1066V1332H0Z" fill="var(--navy)"/>
    <line x1="19" y1="1314" x2="354" y2="1314" stroke="var(--tan)" stroke-width="0.6" opacity=".6"/>
  </svg>

  <section>
    <div class="section-title on-white" style="top:18px;font-size:18px">Tier 3 Bonus Features</div>
    <div class="photo" role="img" aria-label="Navy backdrop with colourful tins behind the brand mark" style="left:-53px;top:57px;width:216px;height:216px;background:radial-gradient(circle at 40% 45%,#3a4063 0%,#252b45 60%,#1c2237 100%)"></div>
    <div class="abs serif" style="left:20px;top:150px;width:96px;text-align:center;font-size:11px;line-height:14px;color:var(--tan)">Harbor<br>and Flint</div>

    <div class="num-badge" style="left:102px;top:64px">01</div>
    <div class="feature-title" style="left:161px;top:73px">Branded Landing Page</div>
    <div class="feature-desc" style="left:161px;top:88px">Created just for your lounge.</div>

    <div class="num-badge" style="left:144px;top:137px">02</div>
    <div class="feature-title" style="left:202px;top:142px">Easter Egg Graphics</div>
    <div class="feature-desc" style="left:202px;top:157px;width:150px">Hidden artwork rewards customers with free cigars when identified.</div>

    <div class="num-badge" style="left:102px;top:210px">03</div>
    <div class="feature-title" style="left:163px;top:212px">Custom Tin Orders</div>
    <div class="feature-desc" style="left:163px;top:228px;width:178px">Eligible with orders of 35+ tins (submit your own artwork) Starting at $375 with a retail value of $875.</div>
  </section>

  <section>
    <div class="section-title on-navy" style="top:358px;font-size:17px">Let’s</div>
    <div class="center-line serif" style="top:380px;font-size:17px;color:var(--white)">CELEBRATE TOGETHER</div>
    <div class="center-line" style="top:418px;font-size:7.6px;font-weight:500;color:var(--tan)">WE’D LOVE TO HELP YOU BRING LANTERN HOURS TO YOUR CUSTOMERS.</div>
    <div class="center-line" style="top:430px;font-size:7.4px;color:var(--white)">Reply to this email or schedule a quick call to explore options and request samples.</div>

    <div class="form-label" style="top:457px">Cheers,</div>
    <div class="field" style="left:31px;top:471px;width:308px;height:22px;padding-top:7px">CSR Name</div>
    <div class="form-label" style="top:499px">KMWR Traders</div>
    <div class="field" style="left:31px;top:515px;width:149px;height:22px;padding-top:7px">CSR Email</div>
    <div class="field" style="left:189px;top:515px;width:150px;height:22px;padding-top:7px">Phone Number</div>
    <div class="field" style="left:31px;top:542px;width:308px;height:41px;padding-top:6px">Company Website or Landing Page</div>
    <div class="pill" style="left:143px;top:592px;width:84px;height:25px;font-size:8.6px">Submit</div>
  </section>

  <section>
    <div class="toro-card" style="left:33px;top:724px">
      <div class="toro-badge" style="left:42px;top:-36px"><span class="cut">TORO</span><span class="size">6 X 54</span></div>
      <div class="toro-title">Connecticut wrapper<br>Ecuador</div>
      <ul class="toro-list" style="left:24px"><li>Habano binder Jalapa</li><li>Filler Esteli and Jalapa</li></ul>
    </div>
    <div class="toro-card" style="left:193px;top:724px">
      <div class="toro-badge" style="left:42px;top:-36px"><span class="cut">TORO</span><span class="size">6 X 54</span></div>
      <div class="toro-title">Habano wrapper<br>Ecuador</div>
      <ul class="toro-list" style="left:18px"><li>Binder Indonesia</li><li>Filler Esteli, Pueblo Nuevo</li></ul>
    </div>
    <div class="toro-card" style="left:33px;top:884px">
      <div class="toro-badge" style="left:42px;top:-36px"><span class="cut">TORO</span><span class="size">6 X 54</span></div>
      <div class="toro-title">Sumatra wrapper<br>Indonesia</div>
      <ul class="toro-list" style="left:24px"><li>Filler habano Ecuador</li><li>Filler Esteli , ometepe</li></ul>
    </div>
    <div class="toro-card" style="left:193px;top:884px">
      <div class="toro-badge" style="left:42px;top:-36px"><span class="cut">TORO</span><span class="size">6 X 54</span></div>
      <div class="toro-title">Maduro wrapper<br>Brazil</div>
      <ul class="toro-list" style="left:25px;top:73px;line-height:10px"><li>Binder Sumatra</li><li style="line-height:10px;padding-top:2px">Filler Esteli , Condega,<br>Jalapa</li></ul>
    </div>
  </section>

  <section>
    <div class="section-title on-navy" style="top:1080px;font-size:17.5px">Packaging</div>
    <div class="abs" style="left:19px;top:1116px;font-size:7.4px;color:var(--white)">Lantern Hours cigars are available in three convenient packaging options:</div>
    <ul class="pack-list">
      <li><span class="pack-name">By the Bundle</span><span class="pack-desc">Ideal for regular smokers who appreciate the value and quality of our cigars.</span></li>
      <li><span class="pack-name">Customized 4-Cigar Lantern Hour Tin</span><span class="pack-desc">Perfect for gifting or special occasions, these tins can be personalized to add a unique touch to your celebration.</span></li>
      <li><span class="pack-name">Custom Box</span><span class="pack-desc">A perfect offering for an event “grab” with all whom you are celebrating with, making it easy to share the joy of Lantern Hours cigars.</span></li>
    </ul>
    <p class="abs" style="left:19px;top:1253px;width:336px;font-size:7.1px;line-height:9.4px;color:var(--white);text-align:justify">Harbor and Flint’s Lantern Hours line is all about celebrating moments, big and small. With a cigar for every time of the day and any special occasion, Lantern Hours ensures that every smoke is a memorable experience. Whether you're on the golf course, the water, a hunt, or just lounging, Lantern Hours cigars are the perfect companions for life's cherished moments.</p>
  </section>
</section>

</body>
</html>
```